Business Card Design Project

A double sided business card for presentation to business leaders in corporate.

Target Market(s)

Corporate, business professionals, HR

Industry/Entity Type

Business

Requirements
Must have
• FRONT

Logo

www.brightfernco.com.au

BACK

Maren Tollvey-Hart
Director

+ 61 (0) 418 556 230
maren@brightfernco.com.au
www.brightfernco.com.au

Impact through energy and employee engagement

("ripples" of logo, bottom corner)

Must be:
- double sided
size: 86 x 54mm
supplied as one pdf with crop marks shown (+- 1mm, with 2-3 mm bleed)

```html
<!DOCTYPE html>
<html lang="en">
<head>
<meta charset="utf-8">
<title>Brightfern Co – Business Card</title>
<link href="https://fonts.googleapis.com/css2?family=Arvo:ital,wght@0,700;1,700&family=Boogaloo&display=swap" rel="stylesheet">
<style>
  :root {
    --page: #ffffff;
    --card: #111011;
    --ground: #242325;
    --foliage: #1c1b1d;
    --brand: #7a3170;
    --ink: #ffffff;
  }
  html, body {
    margin: 0;
    padding: 0;
    width: 1200px;
    height: 1000px;
    overflow: hidden;
    background: var(--page);
  }
  .card {
    position: absolute;
    background: var(--card);
    overflow: hidden;
  }
  .card--front { left: 19px; top: 14px; width: 759px; height: 475px; }
  .card--back  { left: 424px; top: 511px; width: 752px; height: 471px; }

  .meadow {
    position: absolute;
    left: 0; right: 0; bottom: 0;
    background: linear-gradient(to bottom, rgba(36,35,37,0) 0%, var(--foliage) 45%, var(--ground) 80%, var(--ground) 100%);
  }
  .card--front .meadow { top: 90px; }
  .card--back .meadow  { top: 80px; }

  .brand {
    position: absolute;
    display: flex;
    align-items: center;
    font-family: "Arvo", serif;
    font-weight: 700;
    font-style: normal;
    color: var(--brand);
    white-space: nowrap;
  }
  .brand__dot {
    border-radius: 50%;
    background: var(--brand);
    flex: none;
  }
  .card--front .brand { left: 170px; top: 185px; font-size: 64px; gap: 18px; }
  .card--front .brand__dot { width: 34px; height: 34px; }
  .card--back .brand { left: 280px; top: 58px; font-size: 34px; gap: 10px; }
  .card--back .brand__dot { width: 18px; height: 18px; }

  .front-url {
    position: absolute;
    left: 216px; top: 350px;
    font-family: "Boogaloo", sans-serif;
    font-size: 31px;
    color: var(--ink);
    letter-spacing: 0.3px;
  }

  .person {
    position: absolute;
    right: 42px; top: 206px;
    text-align: right;
    font-family: "Arvo", serif;
    font-style: italic;
    font-weight: 700;
    color: var(--ink);
  }
  .person__name { font-size: 27px; letter-spacing: 1px; line-height: 1.1; }
  .person__role { font-size: 19px; margin-top: 4px; }

  .contact {
    position: absolute;
    right: 42px; top: 366px;
    text-align: right;
    font-family: "Arvo", serif;
    font-style: italic;
    font-weight: 700;
    font-size: 16.5px;
    line-height: 22px;
    color: var(--ink);
  }
  .contact p { margin: 0; }
</style>
</head>
<body>
  <section class="card card--front">
    <div class="meadow" role="img" aria-label="Dark silhouettes of wildflowers and grasses across the lower card"></div>
    <div class="brand"><span class="brand__dot"></span>brightfern co</div>
    <div class="front-url">www.brightfernco.com.au</div>
  </section>

  <section class="card card--back">
    <div class="meadow" role="img" aria-label="Dark silhouettes of wildflowers and grasses across the lower card"></div>
    <div class="brand"><span class="brand__dot"></span>brightfern co</div>
    <div class="person">
      <div class="person__name">MAREN TOLLVEY-HART</div>
      <div class="person__role">Director</div>
    </div>
    <div class="contact">
      <p>+ 61 (0) 418 556 230</p>
      <p>maren@brightfernco.com.au</p>
      <p>www.brightfernco.com.au</p>
    </div>
  </section>
</body>
</html>
```